Baked goods front of bag sticker

Toffelwick Brownies,
2 Go size (clear plastic bag of handful of ¼” square bites)
There will also be larger sizes and custom options(corporate/events) using the same image.
Deliverables Needed:
Need sticker with “Toffelwick Brownies” for front of bag, approximate 2” circle or rectangle/square.
Packaging front sticker design should be sizable for other media, ie website, future packaging, logo.
Flavor should be indicated on second sticker that integrates well.
Back sticker is already complete and includes ingredients, company name, health dept permit, and other legal necessities. Font will be changed to integrate with front.
Flavors:
1. Porchlight Caramel Brownie
2. Butterscotch Meadow Brownie
3. Zippity Chocolate
4. Tender Gluten Free (not so gooey but great)
Primary Audiences:
Anyone who wants a sweet treat to enjoy, and maybe share, on the go. Audience wants a fresh treat with real ingredients they know and love (real butter, Pure vanilla, Fresh eggs)
Audience wants something from a baker not a machine.
Sold at checkout in stores that don’t have baked goods, higher end convenience stores, specialty stores, small gourmet stores, theaters, toy stores, sports arenas, etc.
Will be sampled at events (festivals, movie screenings, races)
Tone and Image:
Fresh, Fun and frank with real ingredients you know
Because it is little and is home-baked, it should be perceived as a little treat without the guilt.
Messages:
Fresh, natural, little treat on the run.
Dear Designers,

```html
<!DOCTYPE html>
<html lang="en">
<head>
<meta charset="utf-8">
<title>Toffelwick Brownies – Front Stickers</title>
<link rel="stylesheet" href="https://fonts.googleapis.com/css2?family=Cinzel:wght@600&family=Kaushan+Script&family=Pinyon+Script&display=swap">
<style>
  :root {
    --bg-light: #f4f4f4;
    --bg-mid: #cfd0d2;
    --brown-dark: #5a3418;
    --brown-mid: #7e4c25;
    --brown-light: #8f5a2e;
    --frame-line: #b9865a;
    --cream: #efe6cf;
    --cream-shade: #cdbd96;
    --cream-fold: #a8966c;
    --teal: #2fb3b0;
    --ink: #4a2a12;
  }
  * { margin: 0; padding: 0; box-sizing: border-box; }
  html, body { width: 714px; height: 1200px; overflow: hidden; }
  body {
    position: relative;
    background: radial-gradient(ellipse at 50% 45%, var(--bg-light) 30%, var(--bg-mid) 100%);
  }
  .sticker {
    position: absolute;
    width: 250px;
    height: 250px;
    background: linear-gradient(160deg, var(--brown-light) 0%, var(--brown-mid) 45%, var(--brown-dark) 100%);
    box-shadow: 0 2px 6px rgba(0,0,0,.35);
  }
  .sticker::before {
    content: "";
    position: absolute;
    inset: 9px;
    border: 1.5px solid var(--frame-line);
  }
  .col-left { left: 83px; }
  .col-right { left: 374px; }
  .row-1 { top: 36px; }
  .row-2 { top: 321px; }
  .row-3 { top: 614px; }
  .row-4 { top: 904px; }

  .sticker-art { position: absolute; inset: 0; width: 250px; height: 250px; }

  .home-tag {
    position: absolute;
    top: 16px;
    right: 22px;
    width: 54px;
    text-align: center;
    font-family: "Pinyon Script", cursive;
    font-size: 15px;
    line-height: 16px;
    color: var(--ink);
    padding-top: 6px;
  }
  .brand-name {
    position: absolute;
    left: 22px;
    top: 68px;
    width: 160px;
    font-family: "Cinzel", serif;
    font-weight: 600;
    color: var(--teal);
    font-size: 22px;
    line-height: 24px;
    letter-spacing: .5px;
  }
  .brand-name .brand-sub { display: block; font-size: 14px; padding-left: 60px; }
  .flavor {
    position: absolute;
    left: 22px;
    right: 22px;
    top: 156px;
    text-align: center;
    font-family: "Kaushan Script", cursive;
    font-size: 15px;
    color: var(--ink);
    transform: rotate(-3deg);
    white-space: nowrap;
  }
</style>
</head>
<body>

<svg width="0" height="0" style="position:absolute" aria-hidden="true">
  <defs>
    <symbol id="sticker-shapes" viewBox="0 0 250 250">
      <path d="M168 10 H232 V78 L200 66 L168 78 Z" fill="var(--cream)"/>
      <path d="M0 202 C60 188 140 202 250 172 L250 186 C150 212 70 202 0 216 Z" fill="var(--teal)"/>
      <path d="M4 170 L28 166 L28 202 L4 206 L14 188 Z" fill="var(--cream-shade)"/>
      <path d="M20 194 L28 202 L28 190 Z" fill="var(--cream-fold)"/>
      <path d="M246 130 L222 134 L222 170 L246 166 L236 148 Z" fill="var(--cream-shade)"/>
      <path d="M230 140 L222 134 L222 144 Z" fill="var(--cream-fold)"/>
      <path d="M20 156 C80 140 160 166 230 140 L230 180 C160 204 80 178 20 194 Z" fill="var(--cream)"/>
    </symbol>
  </defs>
</svg>

<div class="sticker col-left row-1">
  <svg class="sticker-art" viewBox="0 0 250 250" aria-hidden="true"><use href="#sticker-shapes"/></svg>
  <div class="home-tag">Home<br>Baked</div>
  <div class="brand-name">Toffelwick<span class="brand-sub">Brownies</span></div>
  <div class="flavor">Porchlight Caramel Brownie</div>
</div>
<div class="sticker col-right row-1">
  <svg class="sticker-art" viewBox="0 0 250 250" aria-hidden="true"><use href="#sticker-shapes"/></svg>
  <div class="home-tag">Home<br>Baked</div>
  <div class="brand-name">Toffelwick<span class="brand-sub">Brownies</span></div>
  <div class="flavor">Butterscotch Meadow Brownie</div>
</div>

<div class="sticker col-left row-2">
  <svg class="sticker-art" viewBox="0 0 250 250" aria-hidden="true"><use href="#sticker-shapes"/></svg>
  <div class="home-tag">Home<br>Baked</div>
  <div class="brand-name">Toffelwick<span class="brand-sub">Brownies</span></div>
  <div class="flavor">Zippity Chocolate</div>
</div>
<div class="sticker col-right row-2">
  <svg class="sticker-art" viewBox="0 0 250 250" aria-hidden="true"><use href="#sticker-shapes"/></svg>
  <div class="home-tag">Home<br>Baked</div>
  <div class="brand-name">Toffelwick<span class="brand-sub">Brownies</span></div>
  <div class="flavor">Tender Gluten Free</div>
</div>

<div class="sticker col-left row-3">
  <svg class="sticker-art" viewBox="0 0 250 250" aria-hidden="true"><use href="#sticker-shapes"/></svg>
  <div class="home-tag">Home<br>Baked</div>
  <div class="brand-name">Toffelwick<span class="brand-sub">Brownies</span></div>
  <div class="flavor">Butterscotch Meadow Brownie</div>
</div>
<div class="sticker col-right row-3">
  <svg class="sticker-art" viewBox="0 0 250 250" aria-hidden="true"><use href="#sticker-shapes"/></svg>
  <div class="home-tag">Home<br>Baked</div>
  <div class="brand-name">Toffelwick<span class="brand-sub">Brownies</span></div>
  <div class="flavor">Porchlight Caramel Brownie</div>
</div>

<div class="sticker col-left row-4">
  <svg class="sticker-art" viewBox="0 0 250 250" aria-hidden="true"><use href="#sticker-shapes"/></svg>
  <div class="home-tag">Home<br>Baked</div>
  <div class="brand-name">Toffelwick<span class="brand-sub">Brownies</span></div>
  <div class="flavor">Zippity Chocolate</div>
</div>
<div class="sticker col-right row-4">
  <svg class="sticker-art" viewBox="0 0 250 250" aria-hidden="true"><use href="#sticker-shapes"/></svg>
  <div class="home-tag">Home<br>Baked</div>
  <div class="brand-name">Toffelwick<span class="brand-sub">Brownies</span></div>
  <div class="flavor">Tender Gluten Free</div>
</div>

</body>
</html>
```